Facebook Header Design Project.

I'm supplying white and colored logos. The Facebook page already exists. URL = https://www.pagebook.example/lumocrest.design The design should not be based on what's already there. Consider mobile implications of the design. This Design will form the designs of other social media headers. LumoCrest is a web design | digital marketing company.

Target Market(s)

People interested in web design | digital marketing services.

Industry/Entity Type

LumoCrest is a web design | digital marketing company. That should be clear in the design.

Colors
0054AA
0677BA
7BADD7
CADEEF
E8F1F8

Requirements
Must have
• Logo. Use Facebook header image dimension.
Nice to have
• Use a color scheme like the logo and feel free to add a color or two from the other side of the color whee.

```html
<!DOCTYPE html>
<html lang="en">
<head>
<meta charset="utf-8">
<title>LumoCrest — Page Header</title>
<link rel="stylesheet" href="https://fonts.googleapis.com/css2?family=Jost:wght@500&family=Exo+2:ital,wght@1,500&display=swap">
<style>
  :root {
    --bg: #2c5699;
    --deep: #0677ba;
    --mid: #7badd7;
    --pale: #cadeef;
    --mist: #e8f1f8;
    --white: #ffffff;
  }
  html, body {
    margin: 0;
    padding: 0;
    overflow: hidden;
    background: var(--bg);
  }
  .header {
    position: relative;
    width: 1200px;
    height: 457px;
    overflow: hidden;
    background: var(--bg);
  }
  .decor {
    position: absolute;
    inset: 0;
  }
  .frame {
    position: absolute;
    left: 51px;
    top: 45px;
    width: 1098px;
    height: 366px;
    border: 1.5px solid rgba(255, 255, 255, 0.85);
    border-radius: 8px;
    background: rgba(255, 255, 255, 0.03);
    box-shadow: 0 0 6px rgba(255, 255, 255, 0.35);
    box-sizing: border-box;
  }
  .brand {
    position: absolute;
    left: 0;
    width: 1200px;
    top: 128px;
    margin: 0;
    text-align: center;
    font-family: "Jost", sans-serif;
    font-weight: 500;
    font-size: 86px;
    line-height: 1;
    color: var(--white);
    letter-spacing: 1px;
  }
  .tagline {
    position: absolute;
    left: 0;
    width: 1200px;
    top: 271px;
    margin: 0;
    text-align: center;
    font-family: "Jost", sans-serif;
    font-weight: 500;
    font-size: 16px;
    letter-spacing: 8.2px;
    color: var(--mist);
  }
  .timeline {
    position: absolute;
    left: 203px;
    top: 327px;
    width: 780px;
    height: 1.5px;
    background: linear-gradient(90deg, var(--deep), var(--mid) 60%, var(--mist));
  }
  .service {
    position: absolute;
    top: 320px;
    width: 0;
  }
  .service .dot {
    position: absolute;
    left: -8px;
    top: 0;
    width: 16px;
    height: 16px;
    border-radius: 50%;
    background: radial-gradient(circle at 35% 35%, var(--mist), var(--mid) 55%, var(--deep));
  }
  .service .label {
    position: absolute;
    left: -120px;
    width: 240px;
    top: 31px;
    text-align: center;
    font-family: "Exo 2", sans-serif;
    font-style: italic;
    font-weight: 500;
    font-size: 14.5px;
    color: var(--white);
    white-space: nowrap;
  }
</style>
</head>
<body>
<div class="header">
  <svg class="decor" width="1200" height="457" viewBox="0 0 1200 457" aria-hidden="true">
    <defs>
      <linearGradient id="blob-top" x1="0" y1="0" x2="1" y2="0">
        <stop offset="0" stop-color="#2a86c6"/>
        <stop offset="1" stop-color="#cadeef"/>
      </linearGradient>
      <linearGradient id="blob-bottom" x1="0" y1="0" x2="1" y2="0">
        <stop offset="0" stop-color="#0677ba"/>
        <stop offset="1" stop-color="#cadeef"/>
      </linearGradient>
    </defs>
    <path d="M0 0 H255 C268 30 262 62 225 74 C190 86 130 78 98 100 C78 114 80 150 62 175 C45 198 20 210 0 214 Z" fill="url(#blob-top)" opacity="0.95"/>
    <path d="M1200 284 C1150 280 1105 292 1088 315 C1072 338 1070 355 1045 360 C1010 366 962 372 940 400 C928 418 924 440 922 457 H1200 Z" fill="url(#blob-bottom)" opacity="0.95"/>
  </svg>

  <div class="frame"></div>

  <h1 class="brand">LumoCrest</h1>
  <p class="tagline">DIGITAL MARKETING COMPANY</p>

  <div class="timeline"></div>
  <div class="service" style="left:203px"><span class="dot"></span><span class="label">Website Design</span></div>
  <div class="service" style="left:378px"><span class="dot"></span><span class="label">Website Development</span></div>
  <div class="service" style="left:600px"><span class="dot"></span><span class="label">Search Engine Optimization</span></div>
  <div class="service" style="left:815px"><span class="dot"></span><span class="label">Digital Marketing</span></div>
  <div class="service" style="left:983px"><span class="dot"></span><span class="label">Graphic Design</span></div>
</div>
</body>
</html>
```